Operator Qualification Testing Flyer

I have a 8x10 basic flyer that I created usin InDesign for one of our services our company provides. I would like to see more options for the layout and general design of the flyer. This flyer will be used as a template for the other services we provide. I will include the InDesign Folder with all the logos and images. Please feel free to use any logo design within the folder and you can change the font and/or colors as needed. I would like the final output in a Indesign package folder to be used in InDesign 2021

Target Market(s)

Business to Business marketing in the Oil and Gas industry

Font styles to use
Sans Serif

Colors
85cae6
85acd3
3377b5
0355a3
0792cd
ffffff
cedeed

Requirements
Must have
• I included/attached a couple of brochures styles that I do like.

```html
<!DOCTYPE html>
<html lang="en">
<head>
<meta charset="utf-8">
<title>Pipeline OQ Testing Flyer</title>
<link href="https://fonts.googleapis.com/css2?family=Open+Sans:wght@400;600;700&family=Arimo:wght@400;700&display=swap" rel="stylesheet">
<style>
  :root {
    --sky: #85cae6;
    --steel: #85acd3;
    --mid-blue: #3377b5;
    --deep-blue: #0355a3;
    --bright-blue: #0792cd;
    --white: #ffffff;
    --mist: #cedeed;
    --ink: #1c1c1c;
    --teal: #1d6f86;
    --body-top: #f7f7f7;
    --body-bottom: #d6d6d6;
  }
  * { box-sizing: border-box; margin: 0; padding: 0; }
  html, body { width: 873px; height: 1200px; overflow: hidden; background: var(--white); }
  .flyer {
    position: relative; width: 873px; height: 1200px; overflow: hidden;
    font-family: "Open Sans", sans-serif; color: var(--ink);
    background: linear-gradient(180deg, var(--white) 0%, var(--body-top) 50%, var(--body-bottom) 100%);
  }
  .header { position: absolute; left: 0; top: 0; width: 873px; height: 196px; background: var(--white); }
  .brand {
    position: absolute; left: 32px; top: 84px;
    display: flex; align-items: center; gap: 12px;
    font-family: "Open Sans", sans-serif; font-weight: 600; font-size: 30px; color: var(--ink);
  }
  .brand-dot { width: 22px; height: 22px; border-radius: 50%; background: var(--teal); }
  .contact {
    position: absolute; right: 18px; top: 146px; text-align: right;
    font-family: "Arimo", sans-serif; font-size: 14px; line-height: 17px; color: var(--teal);
  }
  .band { position: absolute; left: 0; top: 196px; width: 873px; height: 18px; background: var(--sky); }
  .band-lower { position: absolute; left: 0; top: 600px; width: 873px; height: 12px; background: var(--sky); }
  .photo { position: absolute; }
  .photo-trench { left: 0; top: 206px; width: 432px; height: 347px; background: linear-gradient(135deg, #8a7a66, #6e6152 55%, #7f735f); }
  .photo-field { left: 430px; top: 216px; width: 443px; height: 386px; border: 3px solid var(--white); border-right: 0; background: linear-gradient(160deg, #8e806a, #7a6e58 60%, #6f6653); }
  .title-banner { position: absolute; left: 0; top: 552px; width: 590px; height: 80px; }
  .title-banner svg { position: absolute; inset: 0; }
  .title {
    position: absolute; left: 32px; top: 8px;
    font-family: "Open Sans", sans-serif; font-weight: 700; font-size: 47px; letter-spacing: 0.5px;
    color: var(--white); white-space: nowrap;
  }
  .sign { position: absolute; left: 608px; top: 601px; width: 220px; height: 220px; border-radius: 50%; background: radial-gradient(circle, #e2a21c 0%, #d99a17 60%, #1d1a14 66%, #1d1a14 100%); }
  .content { position: absolute; left: 0; top: 0; }
  .section { position: absolute; left: 31px; }
  .section h2 {
    font-family: "Arimo", sans-serif; font-weight: 700; font-size: 26px; line-height: 30px;
    color: var(--bright-blue); margin-bottom: 3px;
  }
  .section p { font-size: 13.4px; line-height: 19.6px; color: var(--ink); }
  .section p + p { margin-top: 10px; }
  .qualification { top: 655px; width: 560px; }
  .qualification p { padding-left: 4px; }
  .covered { top: 843px; width: 480px; }
  .provide { top: 973px; width: 780px; }
</style>
</head>
<body>
<div class="flyer">
  <header class="header">
    <div class="brand"><span class="brand-dot"></span>Ridgeline Field Services Inc.</div>
    <div class="contact">406-555-0172<br>dana@ridgeline-field.co</div>
  </header>
  <div class="band"></div>
  <div class="band-lower"></div>

  <div class="photo photo-trench" role="img" aria-label="Aerial view of an excavator working beside an open pipeline trench with a work truck nearby"></div>
  <div class="photo photo-field" role="img" aria-label="Aerial view of a pipelayer machine at a fenced dig site in a dry field"></div>

  <div class="title-banner">
    <svg width="590" height="80" viewBox="0 0 590 80" aria-hidden="true">
      <polygon points="0,0 590,0 566,80 0,80" fill="var(--deep-blue)"/>
      <polygon points="0,0 590,0 588,7 0,7" fill="var(--mid-blue)"/>
    </svg>
    <h1 class="title">PIPELINE OQ TESTING</h1>
  </div>

  <div class="sign" role="img" aria-label="Round yellow warning sign for a petroleum pipeline"></div>

  <main class="content">
    <section class="section qualification">
      <h2>What Is Operator Qualification?</h2>
      <p>Operator Qualifications (OQ) for DOT Oil/Gas Pipelines are requirements set by Department of Transportation (DOT) and Pipeline and Hazardous Materials Safety Administration (PHMSA). To assure safety in the transport of hazardous gases and liquids in the nation’s pipelines, pipeline operators who perform covered tasks must be qualified. Qualified means that an individual has been evaluated and can perform assigned covered tasks and recognize and react to abnormal operating conditions.</p>
    </section>
    <section class="section covered">
      <h2>What Are Covered Tasks?</h2>
      <p>Covered tasks are defined in an operator’s written plan which defines specific job functions or activities personnel are qualified to perform on a pipeline facility.</p>
    </section>
    <section class="section provide">
      <h2>What We Provide</h2>
      <p>Ridgeline Field Services Inc. utilizes NPTC pipeline program to administer OQ assessment testing on 127 covered tasks. Upon completion of OQ testing the information is first transferred to NPTC’s Registry System and automatically uploaded to SafeLedger.</p>
      <p>In addition to the benefits provided by SafeLedger’s database, the NPTC Registry System houses all the completion information allowing candidates to share their training information and employers to verify successful covered task and level completions.</p>
    </section>
  </main>
</div>
</body>
</html>
```